Marrow Cay Retreat Christmas wishes 2013

We require postcards designed to mail our to our clients for Christmas. We are a SURF travel company, with a high end market and like to mail our Christmas postcards to all our guests that have stayed with us through the year. Front cover will have images and text (ie Seasons Greeting) and our logo. The back will have space for TO: name & address and postage stamp. Will also have some basic text (ie The Management & Staff at Marrow Cay Retreat wish you and your family all the best for the Festive Season and New Year. We look forward to seeing you back at Marrow Cay Retreat again soon etc etc). Here is link to main image https://www.filecrate-demo.net/sh/qwmzrtpl83nvex/Rk7bPoQaZs

Target Market(s)

Our clients are mostly mature men (40-70) surfers who purchase luxury surf trips

Industry/Entity Type

Travel

Requirements
Must have
• Ocean Image (front)
Logo x 2 in same colour - Corvane & Marrow Cay Retreat (front)
Text (front)
Back to be white
Space for name & address (back)
Space for postage stamp (back)
Message (back)
Website www.corvanestays.net (back)

```html
<!DOCTYPE html>
<html lang="en">
<head>
<meta charset="utf-8">
<title>Marrow Cay Retreat — Season's Greetings Postcard</title>
<link rel="stylesheet" href="https://fonts.googleapis.com/css2?family=Raleway:wght@300;400;500&family=Arimo:wght@700&display=swap">
<style>
  :root {
    --backdrop: #e0762a;
    --card-white: #ffffff;
    --sky-top: #3f7fd0;
    --sky-low: #8bb4e6;
    --sea-horizon: #1f5fb0;
    --sea-mid: #1a5aa6;
    --sea-deep: #0f3f7e;
    --front-text: #ffffff;
    --back-text: #8a8a8a;
    --rule: #b9b9b9;
    --url-text: #a3a3a3;
  }
  * { box-sizing: border-box; margin: 0; padding: 0; }
  html, body { width: 1200px; height: 1000px; overflow: hidden; }
  body {
    position: relative;
    background: var(--backdrop);
    font-family: "Raleway", "Helvetica Neue", Arial, sans-serif;
  }

  .postcard { position: absolute; overflow: hidden; }

  /* Front */
  .postcard--front { left: 320px; top: 58px; width: 567px; height: 377px; }
  .front__photo {
    position: absolute; inset: 0;
    background: linear-gradient(180deg,
      var(--sky-top) 0%, var(--sky-low) 20%, #a9c6ec 26%,
      var(--sea-horizon) 27.5%, var(--sea-mid) 45%, #1768b4 65%, var(--sea-deep) 100%);
  }
  .front__greeting {
    position: absolute; left: 57px; top: 46px;
    color: var(--front-text);
    font-weight: 300; font-size: 19px; letter-spacing: 1.2px;
  }
  .front__lodge-name {
    position: absolute; left: 60px; top: 330px; width: 100px;
    text-align: center; color: var(--front-text);
    font-weight: 400; font-size: 9px; letter-spacing: 0.3px;
  }
  .front__brand {
    position: absolute; left: 254px; top: 323px;
    display: flex; align-items: center; gap: 14px;
    color: var(--front-text); font-weight: 400; font-size: 11px; letter-spacing: 1.6px;
  }
  .front__brand-dot { width: 16px; height: 16px; border-radius: 50%; background: var(--front-text); }

  /* Back */
  .postcard--back { left: 325px; top: 490px; width: 562px; height: 375px; background: var(--card-white); }
  .back__message {
    position: absolute; left: 30px; top: 111px; width: 229px;
    color: var(--back-text); font-weight: 400; font-size: 13px; line-height: 17px;
    text-align: justify;
  }
  .back__message p + p { margin-top: 16px; }
  .back__website {
    position: absolute; left: 30px; top: 328px; width: 229px; text-align: center;
    font-family: "Arimo", Arial, sans-serif; font-weight: 700; font-size: 12.5px;
    color: var(--url-text);
  }
  .back__divider { position: absolute; left: 283px; top: 22px; width: 1px; height: 333px; background: var(--rule); }
  .back__divider-mark {
    position: absolute; left: 276px; top: 173px; width: 16px; height: 16px;
    border-radius: 50%; background: var(--rule);
  }
  .back__stamp { position: absolute; left: 489px; top: 20px; width: 45px; height: 71px; }
  .back__address-line { position: absolute; left: 315px; width: 210px; height: 1px; background: var(--rule); }
</style>
</head>
<body>

  <section class="postcard postcard--front">
    <div class="front__photo" role="img" aria-label="Aerial photograph of a calm turquoise ocean under a blue sky with clouds, a distant island and breaking surf, with a swimmer in the foreground"></div>
    <h1 class="front__greeting">SEASON’S GREETINGS!</h1>
    <div class="front__lodge-name">marrowcayretreat.com</div>
    <div class="front__brand">
      <span class="front__brand-dot"></span>
      <span>CORVANE LODGES &amp; RESORTS</span>
    </div>
  </section>

  <section class="postcard postcard--back">
    <div class="back__message">
      <p>The Management &amp; Staff at Marrow Cay Retreat wish you and your family all the best for the Festive Season and New Year.</p>
      <p>We look forward to seeing you back at Marrow Cay Retreat again soon!</p>
    </div>
    <div class="back__website">WWW.CORVANESTAYS.NET</div>
    <div class="back__divider"></div>
    <div class="back__divider-mark"></div>
    <svg class="back__stamp" viewBox="0 0 45 71" aria-label="Postage stamp area">
      <rect x="0.5" y="0.5" width="44" height="70" fill="none" stroke="#c4c4c4" stroke-width="1"/>
      <rect x="3" y="3" width="39" height="65" fill="none" stroke="#c4c4c4" stroke-width="1" stroke-dasharray="2 2"/>
    </svg>
    <div class="back__address-line" style="top:189px"></div>
    <div class="back__address-line" style="top:219px"></div>
    <div class="back__address-line" style="top:249px"></div>
    <div class="back__address-line" style="top:279px"></div>
  </section>

</body>
</html>
```